Graphic Design Project adhesive label

We are a handkerchief wholesaler and require an adhesive sticker to stick on top left side single cello bag 170mm x 170mm. Then to run down the back of back noting our details. Flat and folded inside bag is a floral and or paisley ladies handkerchief.
Sticker approx 30cm wide 90mm long but folded at 45mm. 45mm down the front of bag and 45mm going down back of bag. Changed cm to mm.

Wording for Front sticker:

Harlow Textile
handkerchief
by .Penwick.

Back of sticker:

Made from imported English Harlow Textile
100% cotton traditional hemstitch finish
www.penwick-example.com

Hi - Sorry made a mistake with measurements should be 170 mm not 170cm. Same with sticker mm's.                                     

Reason: Extending deadline as will be away until wednesday 2/5/13

Reason: Have been away and have not had a chance to consider designs, thanks for your patience. T

Target Market(s)

mature generally

Industry/Entity Type

Floral

Requirements
Must have
• prefer a lighter background
Nice to have
• Apart from wording some sort of back ground design, colour or symbol

```html
<!DOCTYPE html>
<html lang="en">
<head>
<meta charset="utf-8">
<title>Harlow Textile Handkerchief – Sticker Label</title>
<link rel="stylesheet" href="https://fonts.googleapis.com/css2?family=EB+Garamond:wght@400;500&display=swap">
<style>
  :root {
    --page: #ffffff;
    --ink: #2e2624;
    --panel-edge: #e2e2e2;
    --band-line: #4a3b35;
    --band-fill: #cbbfb8;
    --petal: #eec7c0;
    --leaf: #c3d3b1;
    --bud: #e8d9a4;
  }
  * { box-sizing: border-box; margin: 0; padding: 0; }
  html, body {
    width: 1200px;
    height: 915px;
    overflow: hidden;
    background: var(--page);
  }
  .sheet {
    position: relative;
    width: 1200px;
    height: 915px;
    font-family: "EB Garamond", Georgia, serif;
    font-variant-numeric: lining-nums;
    color: var(--ink);
  }
  .side-label {
    position: absolute;
    top: 42px;
    width: 200px;
    text-align: center;
    font-size: 26px;
    font-weight: 400;
    letter-spacing: 1px;
  }
  .side-label--front { left: 218px; }
  .side-label--back { left: 786px; }

  .panel {
    position: absolute;
    top: 102px;
    width: 562px;
    height: 789px;
    border: 1px solid var(--panel-edge);
    overflow: hidden;
    background: var(--page);
  }
  .panel--front { left: 37px; }
  .panel--back { left: 605px; }

  .border-band {
    position: absolute;
    left: 0;
    width: 100%;
    height: 26px;
    border-top: 3px solid var(--band-line);
    border-bottom: 3px solid var(--band-line);
  }
  .border-band__fill {
    position: absolute;
    inset: 4px 0;
    background: var(--band-fill);
  }
  .panel--front .border-band { bottom: 0; }
  .panel--back .border-band { top: 0; }

  .floral {
    position: absolute;
  }
  .floral--front {
    left: 0;
    top: 0;
    width: 470px;
    height: 490px;
    background:
      radial-gradient(ellipse 90px 85px at 300px 175px, var(--petal) 60%, transparent 100%),
      radial-gradient(ellipse 50px 55px at 140px 190px, var(--petal) 60%, transparent 100%),
      radial-gradient(ellipse 40px 38px at 170px 330px, var(--petal) 60%, transparent 100%),
      radial-gradient(ellipse 90px 30px at 65px 280px, var(--leaf) 55%, transparent 100%),
      radial-gradient(ellipse 50px 40px at 70px 370px, var(--leaf) 50%, transparent 100%),
      radial-gradient(ellipse 170px 230px at 100px 160px, rgba(195, 211, 177, 0.35) 40%, transparent 100%);
  }
  .floral--back {
    right: 0;
    bottom: 0;
    width: 390px;
    height: 420px;
    background:
      radial-gradient(ellipse 80px 75px at 120px 90px, var(--petal) 60%, transparent 100%),
      radial-gradient(ellipse 50px 50px at 180px 210px, var(--petal) 60%, transparent 100%),
      radial-gradient(ellipse 38px 40px at 40px 290px, var(--petal) 60%, transparent 100%),
      radial-gradient(ellipse 60px 45px at 130px 340px, var(--leaf) 55%, transparent 100%),
      radial-gradient(ellipse 50px 20px at 60px 380px, var(--leaf) 50%, transparent 100%),
      radial-gradient(ellipse 180px 220px at 280px 250px, rgba(195, 211, 177, 0.35) 40%, transparent 100%);
  }

  .front-title {
    position: absolute;
    left: 150px;
    top: 502px;
    width: 365px;
    text-align: center;
    font-weight: 400;
    line-height: 1;
  }
  .front-title__name {
    display: block;
    font-size: 49px;
    line-height: 62px;
  }
  .front-title__maker {
    display: block;
    margin-top: 8px;
    font-size: 34px;
    line-height: 42px;
  }

  .back-copy {
    position: absolute;
    left: 0;
    top: 127px;
    width: 100%;
    text-align: center;
    font-weight: 400;
  }
  .back-copy__detail {
    font-size: 22px;
    line-height: 33px;
  }
  .back-copy__web {
    margin-top: 22px;
    font-size: 26px;
    line-height: 32px;
    letter-spacing: 0.5px;
  }
</style>
</head>
<body>
<main class="sheet">
  <h2 class="side-label side-label--front">FRONT</h2>
  <h2 class="side-label side-label--back">BACK</h2>

  <section class="panel panel--front">
    <div class="floral floral--front" role="img" aria-label="Pastel floral illustration of pink blossoms, green leaves and curling vines"></div>
    <h1 class="front-title">
      <span class="front-title__name">Harlow Textile</span>
      <span class="front-title__name">Handkerchief</span>
      <span class="front-title__maker">by. Penwick</span>
    </h1>
    <div class="border-band">
      <div class="border-band__fill" role="img" aria-label="Ornamental scroll border"></div>
    </div>
  </section>

  <section class="panel panel--back">
    <div class="border-band">
      <div class="border-band__fill" role="img" aria-label="Ornamental scroll border"></div>
    </div>
    <div class="back-copy">
      <p class="back-copy__detail">Made from imported English Harlow fabric</p>
      <p class="back-copy__detail">100% cotton traditional hemstitch finish</p>
      <p class="back-copy__web">www.penwick-example.com</p>
    </div>
    <div class="floral floral--back" role="img" aria-label="Pastel floral illustration of pink blossoms, green leaves and curling vines"></div>
  </section>
</main>
</body>
</html>
```